Primary Home Page Graphic: Crowdfund and Non-Profit Social Promotion Website

WHAT WE NEED: See attached. I need a graphic designed that is comparable to these. The graphic will replace the home page video on our current website Quenvale.com
PREFERRED LOOK: Much like attached. Black/white with color that pops. Must have crowdfunding/non-profit + social media appearance.
WHAT WE DO: Social Promotion of Crowdfunding and Non-Profit Campaigns > the image you design should reflect this subject content.
TEXT ON GRAPHIC:
Your Campaign, Shared.
Get your message moving across social media within minutes.
Thousands of social voices are on stand-by and ready to assist.
Project Deadline Extended
Reason: Not seeing the perfect fit yet for the page. Want to see if we can get some other ideas. Looking for black and white image with title and text displayed in a modern way.
The main graphic needs to appear such as Crowdfunding. Keep the text the same with a call to action.
Please use close attention to detail, modern design technique and good contrast on the colors. Thanks.
Non Profit

```html
<!DOCTYPE html>
<html lang="en">
<head>
<meta charset="utf-8">
<title>Your Campaign Shared – Home Banners</title>
<link href="https://fonts.googleapis.com/css2?family=Amatic+SC:wght@700&family=Patrick+Hand+SC&display=swap" rel="stylesheet">
<style>
  :root {
    --page-bg: #ffffff;
    --teal: #2bd0d9;
    --white: #ffffff;
    --ink: #111111;
    --disc: rgba(17, 17, 17, 0.88);
    --label: #e9e9e9;
    --dot: #9a9a9a;
  }
  html, body {
    margin: 0;
    width: 1200px;
    height: 1200px;
    overflow: hidden;
    background: var(--page-bg);
  }
  .banner {
    position: absolute;
    left: 44px;
    width: 1112px;
    height: 494px;
    overflow: hidden;
    box-shadow: 0 3px 8px rgba(0, 0, 0, 0.35);
  }
  .banner--planting { top: 84px; }
  .banner--crowd { top: 622px; }
  .banner__photo {
    position: absolute;
    inset: 0;
  }
  .banner--planting .banner__photo {
    background:
      radial-gradient(ellipse at 80% 45%, rgba(150,150,150,0.55), transparent 45%),
      radial-gradient(ellipse at 25% 60%, rgba(110,110,110,0.5), transparent 50%),
      linear-gradient(100deg, #3a3a3a 0%, #4b4b4b 45%, #6a6a6a 75%, #2c2c2c 100%);
  }
  .banner--crowd .banner__photo {
    background:
      radial-gradient(ellipse at 20% 55%, rgba(170,170,170,0.5), transparent 40%),
      radial-gradient(ellipse at 85% 50%, rgba(140,140,140,0.45), transparent 40%),
      linear-gradient(180deg, #7a7a7a 0%, #4a4a4a 40%, #262626 100%);
  }
  .banner__art {
    position: absolute;
    inset: 0;
  }
  .banner__title {
    position: absolute;
    left: 0;
    right: 0;
    top: 44px;
    margin: 0;
    text-align: center;
    font-family: "Amatic SC", cursive;
    font-weight: 700;
    font-size: 90px;
    line-height: 1;
    letter-spacing: 2px;
    text-transform: uppercase;
    white-space: nowrap;
    color: var(--white);
    text-shadow: 0 2px 4px rgba(0, 0, 0, 0.4);
  }
  .banner__copy {
    position: absolute;
    left: 442px;
    width: 240px;
    margin: 0;
    text-align: center;
    font-family: "Patrick Hand SC", cursive;
    font-size: 19px;
    line-height: 25px;
    text-transform: uppercase;
    white-space: nowrap;
  }
  .banner__copy--lead { top: 134px; color: var(--teal); }
  .banner__copy--support { top: 219px; color: var(--white); }
  .feature-label {
    position: absolute;
    top: 424px;
    width: 200px;
    margin: 0;
    text-align: center;
    font-family: "Patrick Hand SC", cursive;
    font-size: 14px;
    line-height: 18px;
    letter-spacing: 1px;
    text-transform: uppercase;
    white-space: nowrap;
    color: var(--label);
  }
  .feature-label--funding { left: 188px; }
  .feature-label--nonprofit { left: 384px; }
  .feature-label--voice { left: 576px; }
  .cta {
    position: absolute;
    left: 779px;
    top: 298px;
    width: 150px;
    height: 150px;
    display: flex;
    align-items: center;
    justify-content: center;
    text-align: center;
    font-family: "Patrick Hand SC", cursive;
    font-size: 27px;
    line-height: 29px;
    text-transform: uppercase;
    white-space: nowrap;
    color: var(--teal);
    text-decoration: none;
    transform: rotate(8deg);
  }
</style>
</head>
<body>

<svg width="0" height="0" style="position:absolute" aria-hidden="true">
  <defs>
    <g id="person">
      <circle cx="0" cy="-16" r="10"/>
      <path d="M-15 -2 Q-15 -6 -11 -6 H11 Q15 -6 15 -2 V18 Q15 20 13 20 H-13 Q-15 20 -15 18 Z"/>
    </g>
    <g id="banner-graphics">
      <circle cx="562" cy="221" r="136" fill="var(--disc)"/>
      <circle cx="562" cy="221" r="126" fill="none" stroke="#dcdcdc" stroke-width="1.5" stroke-dasharray="6 5"/>
      <line x1="360" y1="396" x2="640" y2="396" stroke="var(--dot)" stroke-width="4" stroke-linecap="round" stroke-dasharray="0.1 10"/>
      <g fill="var(--teal)">
        <use href="#person" x="263" y="338"/>
        <use href="#person" x="311" y="338"/>
        <use href="#person" x="239" y="388"/>
        <use href="#person" x="287" y="388"/>
        <use href="#person" x="337" y="388"/>
      </g>
      <g fill="var(--teal)">
        <ellipse cx="480" cy="372" rx="46" ry="36"/>
        <ellipse cx="436" cy="372" rx="10" ry="13"/>
        <path d="M452 344 L446 322 L466 338 Z"/>
        <rect x="452" y="396" width="14" height="16" rx="3"/>
        <rect x="494" y="396" width="14" height="16" rx="3"/>
        <path d="M524 362 q12 -4 8 -14" fill="none" stroke="var(--teal)" stroke-width="4" stroke-linecap="round"/>
        <circle cx="491" cy="324" r="14"/>
      </g>
      <circle cx="458" cy="362" r="3" fill="var(--ink)"/>
      <path d="M470 346 q20 -10 42 0" fill="none" stroke="var(--ink)" stroke-width="4" stroke-linecap="round"/>
      <text x="491" y="331" text-anchor="middle" font-family="Patrick Hand SC, cursive" font-size="20" fill="var(--ink)">$</text>
      <g fill="var(--teal)">
        <path d="M622 368 Q622 350 640 350 L660 350 L704 318 Q716 312 716 326 V412 Q716 426 704 420 L660 390 L640 390 Q622 390 622 372 Z"/>
        <path d="M640 392 H664 L670 418 Q671 424 665 424 H647 Q641 424 640 418 Z"/>
        <ellipse cx="722" cy="369" rx="12" ry="50"/>
      </g>
      <ellipse cx="722" cy="369" rx="5" ry="24" fill="var(--ink)"/>
      <rect x="726" y="360" width="8" height="18" rx="3" fill="var(--teal)"/>
      <circle cx="854" cy="373" r="75" fill="var(--white)"/>
      <circle cx="854" cy="373" r="67" fill="none" stroke="#555555" stroke-width="1.2" stroke-dasharray="5 4"/>
    </g>
  </defs>
</svg>

<section class="banner banner--planting">
  <div class="banner__photo" role="img" aria-label="Black and white photo: hands planting a seedling in soil, and a smiling woman taking a phone picture by a harbour"></div>
  <svg class="banner__art" width="1112" height="494" viewBox="0 0 1112 494" aria-hidden="true"><use href="#banner-graphics"/></svg>
  <h1 class="banner__title">Your Campaign Shared</h1>
  <p class="banner__copy banner__copy--lead">Get your message<br>moving across social<br>media within minutes.</p>
  <p class="banner__copy banner__copy--support">Thousands of social<br>voices are on stand-by<br>and ready to assist.</p>
  <p class="feature-label feature-label--funding">Crowd<br>Funding</p>
  <p class="feature-label feature-label--nonprofit">Non-Profit<br>Organisations</p>
  <p class="feature-label feature-label--voice">Expanded Voice<br>Through Social Media</p>
  <a class="cta" href="#start">Let's Get<br>Started</a>
</section>

<section class="banner banner--crowd">
  <div class="banner__photo" role="img" aria-label="Black and white photo: a group of cheering young friends joining hands in a street"></div>
  <svg class="banner__art" width="1112" height="494" viewBox="0 0 1112 494" aria-hidden="true"><use href="#banner-graphics"/></svg>
  <h1 class="banner__title">Your Campaign Shared</h1>
  <p class="banner__copy banner__copy--lead">Get your message<br>moving across social<br>media within minutes.</p>
  <p class="banner__copy banner__copy--support">Thousands of social<br>voices are on stand-by<br>and ready to assist.</p>
  <p class="feature-label feature-label--funding">Crowd<br>Funding</p>
  <p class="feature-label feature-label--nonprofit">Non-Profit<br>Organisations</p>
  <p class="feature-label feature-label--voice">Expanded Voice<br>Through Social Media</p>
  <a class="cta" href="#start">Let's Get<br>Started</a>
</section>

</body>
</html>
```